Wolken am fernen Meer
Fox7moon ist sehr flexibel und zeitnah auf alle Änderungswünsche eingegangen und hat ein tolles feeling für Layout. Jederzeit wieder. Danke für die tolle Zusammenarbeit
Zielgruppe
Ein spiritueller Roman, der im Jenseits und im Diesseits spielt.
Zielgruppe Frauen ab 35. Ist in Deutschland veröffentlicht.
Soll jetzt noch in anderen Ländern z.B. USA veröffentlicht werden.
Aufgabenstellung
1)Allgemein:
Covergestaltung erst einmal für Print (wird dann von Print Harbor, bzw. Press by Order ) an elumo automatisch übertragen. Möchte bestehendes cover ersetzen: http://www.warenfluss-beispiel.de/Wolken-am-fernen-Meer-Reiseerz%C3%A4hlung/dp/3998150216/ref=sr_1_1?ie=UTF8&qid=1443180155&sr=8-1&keywords=mira+solberg
2) Formate:
Deutsche Fassung: Format: 13,5x21,5 cm / PbO,
Englische Fassung: 13.97 x 21.59 cm /Print Harbor - Warenfluss)
3) Inhaltliche Wünsche:
a. Covervorderseite: komplettes Bild (Datei `Wiese´) über das gesamte Cover ziehen. Titel und Untertitel wo sich der Himmel befindet (Beispiel Datei `Eigenversuch´).
b. Ergänzung der Datei Wiese um eine kleine `geisterhafte Tür (eine die nicht so stark auffällt). Wo: mittig im Licht direkt über der Wiese. dort, wo das Licht ist, direkt mittig auf der Wiese (Beispiel: ähnlich wie in der beigefügten Datei `Türe´)
c. Coverrückseite: Schemenhafte Spiegelung der Vorderseite (Beispiel: Datei: Book-Cover-Review).
4) nähere Info zum Hintergrund: www.mirasolberg-beispiel.com
5) Folgende Dateien brauche ich:
- zwei PDF-Dateien (einmal die deutsche + einmal die englische Fassung) von dem fertigen Cover inkl. Buchrücken und so weiter
- Eine JEPG-Datei von dem Bild mit Tür und Text (einmal deutsch, einmal englisch)
- eine JEPG-Datei nur von dem Bild mit Tür
6) Anhänge
- Bilddatei Wiese
- Bilddatei Tür
- Beispieldatei `Eigenversuch´
- Infodatei: Titel, Untertitel, Buchrückentext für deutsche und englische Fassung

```html
<!DOCTYPE html>
<html lang="de">
<head>
<meta charset="utf-8">
<title>Wolken am fernen Meer – Buchumschlag</title>
<link href="https://fonts.googleapis.com/css2?family=PT+Sans:wght@700&family=Patrick+Hand&family=Open+Sans:ital,wght@0,400;1,600&family=EB+Garamond&display=swap" rel="stylesheet">
<style>
  :root {
    --ink-navy: #2d2f6a;
    --white: #ffffff;
    --sky-top: #8d9bb6;
    --sky-mid: #c9c9cf;
    --glow: #f7efc6;
    --meadow-light: #c9d08e;
    --meadow-dark: #7f9645;
    --shadow: rgba(40, 40, 60, 0.55);
  }
  * { margin: 0; padding: 0; box-sizing: border-box; }
  html, body { width: 1200px; height: 955px; overflow: hidden; background: #ffffff; }
  .cover-wrap { position: relative; width: 1200px; height: 955px; overflow: hidden; }

  .scene {
    position: absolute; inset: 0;
    background:
      radial-gradient(ellipse 260px 220px at 880px 560px, rgba(255,248,210,0.95), rgba(255,244,200,0) 70%),
      linear-gradient(180deg, var(--sky-top) 0%, var(--sky-mid) 35%, var(--glow) 62%, var(--meadow-light) 74%, var(--meadow-dark) 100%);
  }
  .back-veil {
    position: absolute; left: 0; top: 0; width: 582px; height: 955px;
    background: linear-gradient(180deg, rgba(255,255,255,0.35) 0%, rgba(255,255,255,0.5) 60%, rgba(255,255,255,0.35) 100%);
  }

  .blurb {
    position: absolute; left: 56px; width: 488px;
    font-family: "Open Sans", sans-serif; font-size: 13.4px; line-height: 17px;
    color: var(--ink-navy); text-align: justify; hyphens: auto;
  }
  .blurb p + p { margin-top: 9px; }
  .blurb--story { top: 53px; }
  .blurb--author { top: 462px; }

  .ean-box {
    position: absolute; left: 347px; top: 806px; width: 215px; height: 107px;
    background: var(--white); padding: 14px 20px;
    font-family: "EB Garamond", serif; font-size: 17px; color: #111;
  }

  .spine-title, .spine-author {
    position: absolute; left: 603px; writing-mode: vertical-rl;
    color: var(--white); text-shadow: 1px 1px 3px var(--shadow);
    transform: translateX(-50%);
  }
  .spine-title { top: 51px; font-family: "Patrick Hand", cursive; font-size: 36px; }
  .spine-author { top: 757px; font-family: "PT Sans", sans-serif; font-weight: 700; font-size: 31px; }

  .front-text { position: absolute; left: 612px; width: 582px; text-align: center; color: var(--white); }
  .title { top: 186px; font-family: "Patrick Hand", cursive; font-weight: 400; font-size: 48px; line-height: 56px; text-shadow: 2px 2px 4px var(--shadow); letter-spacing: 0.5px; }
  .subtitle { top: 243px; font-family: "Open Sans", sans-serif; font-style: italic; font-weight: 600; font-size: 22px; text-shadow: 1px 1px 3px var(--shadow); }
  .author { top: 880px; font-family: "PT Sans", sans-serif; font-weight: 700; font-size: 28px; text-shadow: 1px 1px 3px var(--shadow); }
</style>
</head>
<body>
<div class="cover-wrap">
  <div class="scene" role="img" aria-label="Foto einer Sommerwiese mit Mohnblumen, Kamille und Kornblumen unter lichtem Himmel, in der Mitte eine geisterhafte helle Tür im Gegenlicht; auf der Rückseite schemenhaft gespiegelt"></div>
  <div class="back-veil"></div>

  <div class="blurb blurb--story">
    <p>Nach einem Unfall auf der Küstenstraße erwacht Marta nicht am Strand, sondern an einem stillen Ort zwischen den Welten - und merkt: das Ende ist gar kein Ende…und `das Loslassen ist eigentlich ganz leicht´.</p>
    <p>Ganz anders als ihr bisheriges Leben. Dort musste Marta immer ringen - als Mädchen um die Aufmerksamkeit ihres Vaters, als junge Frau um einen Platz in der Welt mit dem Gefühl nie genug zu sein, als berufstätige Mutter gegen die ständige Müdigkeit und zuletzt gegen die Angst vor dem Alleinsein.</p>
    <p>Am Ufer begegnet Marta der Wegweiserin Elva, die sie über einem Meer aus Wolken in Empfang nimmt. Elva zeigt ihr die fremde Landschaft und begleitet sie durch rätselhafte, erschreckende und wunderschöne Begegnungen. Beim Blick zurück auf ihre Jahre gewinnt Marta neue Einsichten in ihr Wesen und ihre Wege. Verbindungen im `Gewebe´ des Lebens werden nun sichtbar und vieles bekommt rückblickend eine Bedeutung.</p>
    <p>Martas Sohn Jonas versucht unterdessen zu Hause mit seinem Schmerz fertig zu werden und das Erbe seiner Mutter zu ordnen. Am Ende blicken beide auf ihre gemeinsamen Jahre als Mutter und Sohn: Jonas in dieser Welt, Marta in der anderen und gemeinsam an einem Strand, den Jonas in seinen Träumen erreicht.</p>
  </div>

  <div class="blurb blurb--author">
    <p>Nach dem Abschied von ihrer Großmutter beschäftigte sich die Autorin lange mit der Frage, was nach dem Leben kommt. Ihre Gedanken und die eigene Erfahrung mit der Trauer formte sie zu dieser `Erzählung vom leisen Übergang´.</p>
    <p>Das Ende ist kein Abbruch. Es ist eine Schwelle zwischen zwei Ufern. Trauernde finden in dieser kleinen Geschichte ein Bild, wie das Dasein der Verstorbenen aussehen könnte - aber nicht muss - denn vielleicht ist alles ganz anders! Bestimmte Glaubensrichtungen stehen hier nicht im Mittelpunkt. Jede Leserin kann sich - gleich welche Weltanschauung und welche Vorstellungen sie mitbringt - dazu einladen lassen, das eigene Leben aus einem neuen Blickwinkel zu sehen und sich als Teil eines größeren Ganzen zu erleben.</p>
  </div>

  <div class="ean-box">EAN Code</div>

  <div class="spine-title">Wolken am fernen Meer</div>
  <div class="spine-author">Mira Solberg</div>

  <h1 class="front-text title">Wolken am fernen Meer</h1>
  <p class="front-text subtitle">Eine Erzählung vom leisen Übergang</p>
  <p class="front-text author">Mira Solberg</p>
</div>
</body>
</html>
```